Audio Visual company needs brochure design

We are an AV company that does Audio Visual work solely for Commercial customers. We Design, sale and install various Audio Visual systems for our customers. This may be something as simple as a conference room, a new sound system for a church or a new sound, lighting and video system for an arena or stadium.

We don't really have any ideas in mind and that's the reason we are turning to you. We want something that highlights what we do, and something they will look at - not just toss in the can.

Included is a copy of our logo (sorry it's the only copy we have now)

Our company name is Velmira Staging www.velmirastaging.example
Updates

Reason: The rest of our management team hasn't provided feedback to me yet. We will pick the design this week.

Target Market(s)

70% of our business is churches and the remaining is corporate customers and restaurants.

Industry/Entity Type

Church

Requirements
Must have
• The brochure will be 8.5" x 11" printed both sides - open to Z fold or Tri fold designs. We can provide pictures of our work if needed - though they may not be the best.
Should not have
• No generic pictures of just speakers, projectors, microphones, etc.

```html
<!DOCTYPE html>
<html lang="en">
<head>
<meta charset="utf-8">
<title>Velmira Staging – Tri-fold Brochure</title>
<link href="https://fonts.googleapis.com/css2?family=Open+Sans:wght@400;600;700&display=swap" rel="stylesheet">
<style>
  :root{
    --navy:#2f3b73;
    --navy-deep:#25306a;
    --navy-light:#b9c3e6;
    --green:#8ba33b;
    --ink:#3a3a3a;
    --muted:#5c5c5c;
    --paper:#ffffff;
    --gray-top:#f2f2f2;
    --gray-bottom:#c9c9c9;
    --bg:#e9e7e4;
    --photo-a:#6b4a34;
    --photo-b:#b9a99a;
    --accent-red:#c44a3a;
  }
  *{box-sizing:border-box;margin:0;padding:0}
  html,body{width:1200px;height:960px;overflow:hidden}
  body{background:var(--bg);font-family:"Open Sans",Arial,sans-serif;color:var(--ink)}
  .canvas{position:relative;width:1200px;height:960px;display:flex;align-items:center;justify-content:center;gap:40px}
  .spread{display:flex;background:var(--paper);padding:8px 8px 22px;box-shadow:0 6px 18px rgba(0,0,0,.18)}
  .panel{position:relative;width:180px;height:480px;overflow:hidden}
  .panel--navy{background:var(--navy);color:#fff}
  .photo{display:block;height:150px;margin:10px 10px 0;border:3px solid #f4efe9;background:linear-gradient(180deg,var(--photo-a),var(--photo-b) 70%,#7a5a48)}
  .panel-title{font-size:11.5px;font-weight:600;letter-spacing:.5px;text-align:center;margin:48px 0 20px}
  .body-copy{font-size:6.8px;line-height:1.38;text-align:justify;padding:0 14px;margin-bottom:8px}
  .url-band{position:absolute;left:0;right:0;bottom:0;height:20px;background:var(--green);color:#fff;font-size:7.5px;letter-spacing:.6px;display:flex;align-items:center;justify-content:center}
  .panel--contact{background:linear-gradient(180deg,var(--gray-top),#e6e6e6 45%,var(--gray-bottom))}
  .contact-head{color:var(--green);font-size:7.2px;font-weight:700;text-align:center;margin:140px 0 12px}
  .region{text-align:center;font-size:5.9px;color:var(--muted);line-height:1.4;margin-bottom:7px}
  .region strong{display:block;font-size:7.5px;color:var(--ink);font-weight:700}
  .contact-name{position:absolute;bottom:36px;left:0;right:0;text-align:center;font-size:10.5px;font-weight:700;color:#1f1f1f}
  .contact-name .dot{display:inline-block;width:8px;height:8px;background:#1f1f1f;border-radius:50%;margin-right:5px}
  .panel--cover{background:linear-gradient(180deg,var(--navy-light) 0%,#6f7eb8 25%,var(--navy) 60%,var(--navy-deep));color:#fff}
  .cover-name{position:absolute;top:236px;left:0;right:0;text-align:center;font-size:14px;font-weight:700}
  .cover-tagline{position:absolute;top:264px;left:0;right:0;text-align:center;font-size:6.5px;color:#dfe4f5}
  .cover-tagline span{margin:0 3px}
  .cover-url{position:absolute;bottom:6px;left:0;right:0;text-align:center;font-size:6.5px;color:rgba(255,255,255,.35);letter-spacing:.5px}
  .panel--intro{background:var(--paper);padding-right:8px}
  .panel--intro .photo{margin:0;height:130px;border:none}
  .intro-title{display:inline-block;margin:10px 0 12px;padding:3px 24px 3px 8px;font-size:7.5px;font-weight:700;color:var(--accent-red);background:linear-gradient(90deg,#f3e3e0,#fff);letter-spacing:.3px}
  .panel--intro .body-copy{color:var(--muted);padding:0 4px}
</style>
</head>
<body>
<main class="canvas">
  <section class="spread spread--outside" aria-label="Brochure outside">
    <article class="panel panel--navy">
      <div class="photo" role="img" aria-label="Church sanctuary with installed lighting and sound system"></div>
      <h2 class="panel-title">WHO WE ARE</h2>
      <p class="body-copy">Lorem ipsum dolor sit amet, consectetuer adipiscing elit, sed diam nonummy nibh euismod tincidunt ut laoreet dolore magna aliquam erat volutpat.</p>
      <p class="body-copy">Ut wisi enim ad minim veniam, quis nostrud exerci tation ullamcorper suscipit lobortis nisl ut aliquip ex ea commodo consequat. Duis autem vel eum iriure dolor in hendrerit in vulputate velit esse molestie consequat, vel illum dolore eu feugiat nulla facilisis at vero eros et accumsan et iusto odio dignissim qui blandit praesent luptatum zzril delenit augue duis dolore te feugait nulla facilisi.</p>
      <div class="url-band">www.velmirastaging.example</div>
    </article>
    <article class="panel panel--contact">
      <h2 class="contact-head">NEED TO GET IN TOUCH IN YOUR REGION?</h2>
      <p class="region"><strong>Cincinnati</strong>Call Us: 513 555 0142<br>Write Us: sales@velmirastaging.example</p>
      <p class="region"><strong>Columbus</strong>Call Us: 614 555 0187<br>Write Us: columbus@velmirastaging.example</p>
      <p class="region"><strong>Dayton</strong>Call Us: 937 555 0163<br>Write Us: dayton@velmirastaging.example</p>
      <p class="region"><strong>Indianapolis</strong>Call Us: 317 555 0129<br>Write Us: indy@velmirastaging.example</p>
      <p class="region"><strong>Louisville</strong>Call Us: 502 555 0174<br>Write Us: louisville@velmirastaging.example</p>
      <div class="contact-name"><span class="dot"></span>Velmira Staging</div>
      <div class="url-band">www.velmirastaging.example</div>
    </article>
    <article class="panel panel--cover">
      <div class="cover-name">Velmira Staging</div>
      <div class="cover-tagline"><span>Innovation</span>|<span>Motivation</span>|<span>Satisfaction</span></div>
      <div class="cover-url">www.velmirastaging.example</div>
    </article>
  </section>

  <section class="spread spread--inside" aria-label="Brochure inside">
    <article class="panel panel--contact">
      <h2 class="contact-head">NEED TO GET IN TOUCH IN YOUR REGION?</h2>
      <p class="region"><strong>Cincinnati</strong>Call Us: 513 555 0142<br>Write Us: sales@velmirastaging.example</p>
      <p class="region"><strong>Columbus</strong>Call Us: 614 555 0187<br>Write Us: columbus@velmirastaging.example</p>
      <p class="region"><strong>Dayton</strong>Call Us: 937 555 0163<br>Write Us: dayton@velmirastaging.example</p>
      <p class="region"><strong>Indianapolis</strong>Call Us: 317 555 0129<br>Write Us: indy@velmirastaging.example</p>
      <p class="region"><strong>Louisville</strong>Call Us: 502 555 0174<br>Write Us: louisville@velmirastaging.example</p>
      <div class="contact-name"><span class="dot"></span>Velmira Staging</div>
      <div class="url-band">www.velmirastaging.example</div>
    </article>
    <article class="panel panel--intro">
      <div class="photo" role="img" aria-label="Church auditorium with seating rows and a cross on the front wall"></div>
      <h2 class="intro-title">INTRODUCTION</h2>
      <p class="body-copy">Lorem ipsum dolor sit amet, consectetuer adipiscing elit, sed diam nonummy nibh euismod tincidunt ut laoreet dolore magna aliquam erat volutpat.</p>
      <p class="body-copy">Ut wisi enim ad minim veniam, quis nostrud exerci tation ullamcorper suscipit lobortis nisl ut aliquip ex ea commodo consequat. Duis autem vel eum iriure dolor in hendrerit in vulputate velit esse molestie consequat, vel illum dolore eu feugiat nulla facilisis at vero eros et accumsan et iusto odio dignissim qui blandit praesent luptatum zzril delenit augue duis dolore te feugait nulla facilisi.</p>
      <p class="body-copy">Nam liber tempor cum soluta nobis eleifend option congue nihil imperdiet doming id quod mazim placerat facer possim assum. Typi non habent claritatem insitam; est usus legentis in iis qui facit eorum claritatem.</p>
      <p class="body-copy">Mirum est notare quam littera gothica, quam nunc putamus parum claram, anteposuerit litterarum formas humanitatis per seacula quarta decima et quinta decima.</p>
      <p class="body-copy">Eodem modo typi, qui nunc nobis videntur parum clari, fiant sollemnes in futurum.</p>
    </article>
    <article class="panel panel--navy">
      <div class="photo" role="img" aria-label="Church sanctuary with installed lighting and sound system"></div>
      <h2 class="panel-title">WHO WE ARE</h2>
      <p class="body-copy">Lorem ipsum dolor sit amet, consectetuer adipiscing elit, sed diam nonummy nibh euismod tincidunt ut laoreet dolore magna aliquam erat volutpat.</p>
      <p class="body-copy">Ut wisi enim ad minim veniam, quis nostrud exerci tation ullamcorper suscipit lobortis nisl ut aliquip ex ea commodo consequat. Duis autem vel eum iriure dolor in hendrerit in vulputate velit esse molestie consequat, vel illum dolore eu feugiat nulla facilisis at vero eros et accumsan et iusto odio dignissim qui blandit praesent luptatum zzril delenit augue duis dolore te feugait nulla facilisi.</p>
      <div class="url-band">www.velmirastaging.example</div>
    </article>
  </section>
</main>
</body>
</html>
```